Dalton Power Supply, Inc. Business Card Design

We are an Electrical Distributor looking for a Modern, Professional Business Card design.

Target Market(s)

Residential Commercial Industrial

Industry/Entity Type

Electrical

Contact Information for Business Card

Dalton Power Supply, Inc.
418 Maple Ridge Lane
Brookvale, NC 27514
555-214-7630
555-214-8842 Fax
daltonpower@brightmail-example.net

```html
<!DOCTYPE html>
<html lang="en">
<head>
<meta charset="utf-8">
<title>Dalton Power Supply, Inc. – Business Card</title>
<link rel="stylesheet" href="https://fonts.googleapis.com/css2?family=Oswald:wght@300;500&display=swap">
<style>
  :root {
    --stage: #e4e2df;
    --card-white: #ffffff;
    --brand-red: #b3222a;
    --brand-yellow: #f5c000;
    --ink-light: #ffffff;
  }
  * { box-sizing: border-box; margin: 0; padding: 0; }
  html, body {
    width: 1200px;
    height: 813px;
    overflow: hidden;
    background: var(--stage);
  }
  .stage {
    width: 1200px;
    height: 813px;
    display: flex;
    align-items: center;
    justify-content: center;
  }
  .business-card {
    width: 1000px;
    height: 572px;
    background: var(--card-white);
    display: flex;
    flex-direction: column;
    box-shadow: 0 10px 30px rgba(0,0,0,0.18);
    font-family: "Oswald", sans-serif;
    font-weight: 300;
  }
  .card-header {
    height: 220px;
    display: flex;
    align-items: center;
    justify-content: center;
    gap: 22px;
  }
  .brand-dot {
    width: 62px;
    height: 62px;
    border-radius: 50%;
    background: var(--brand-red);
  }
  .brand-name {
    font-weight: 500;
    font-size: 64px;
    letter-spacing: 1px;
    color: var(--brand-yellow);
    text-transform: uppercase;
  }
  .card-body {
    flex: 1;
    background: var(--brand-red);
    color: var(--ink-light);
    display: flex;
    align-items: center;
    justify-content: center;
    padding: 0 40px;
  }
  .address {
    text-align: right;
    font-size: 31px;
    line-height: 1.3;
    padding-right: 30px;
  }
  .divider {
    width: 2px;
    align-self: stretch;
    margin: 70px 0;
    background: var(--ink-light);
  }
  .contact-list {
    list-style: none;
    padding-left: 26px;
    font-size: 30px;
    line-height: 1.2;
  }
  .contact-item {
    display: flex;
    align-items: center;
    gap: 14px;
    margin: 8px 0;
  }
  .contact-icon {
    width: 40px;
    height: 40px;
    flex: none;
  }
</style>
</head>
<body>
<main class="stage">
  <article class="business-card">
    <header class="card-header">
      <span class="brand-dot"></span>
      <span class="brand-name">Dalton Power Supply</span>
    </header>
    <section class="card-body">
      <address class="address" style="font-style:normal">
        Dalton Power Supply, Inc.<br>
        418 Maple Ridge Lane<br>
        Brookvale, NC 27514
      </address>
      <div class="divider"></div>
      <ul class="contact-list">
        <li class="contact-item">
          <svg class="contact-icon" viewBox="0 0 40 40" aria-hidden="true">
            <circle cx="20" cy="20" r="20" fill="#fff"/>
            <path d="M14 11c1-1 2-1 3 0l2 3c.6 1 .4 2-.4 2.6l-1.2 1c1 2.4 2.6 4 5 5l1-1.2c.6-.8 1.6-1 2.6-.4l3 2c1 1 1 2 0 3l-1.5 1.5c-1.5 1.5-5 .5-8.5-3S10.5 16 12 14.5z" fill="var(--brand-red)"/>
          </svg>
          <span>555-214-7630</span>
        </li>
        <li class="contact-item">
          <svg class="contact-icon" viewBox="0 0 40 40" aria-hidden="true">
            <circle cx="20" cy="20" r="20" fill="#fff"/>
            <rect x="14" y="9" width="12" height="8" fill="var(--brand-red)"/>
            <rect x="10" y="17" width="20" height="13" rx="2" fill="var(--brand-red)"/>
            <rect x="14" y="23" width="12" height="2" fill="#fff"/>
          </svg>
          <span>555-214-8842</span>
        </li>
        <li class="contact-item">
          <svg class="contact-icon" viewBox="0 0 40 40" aria-hidden="true">
            <circle cx="20" cy="20" r="20" fill="#fff"/>
            <rect x="9" y="13" width="22" height="15" rx="1.5" fill="var(--brand-red)"/>
            <path d="M9.5 14l10.5 8 10.5-8" fill="none" stroke="#fff" stroke-width="1.6"/>
          </svg>
          <span>daltonpower@brightmail-example.net</span>
        </li>
      </ul>
    </section>
  </article>
</main>
</body>
</html>
```